Banner Ad Design Project

My online radio station features DJ sets periodically. The series is called "Deep Orbit" I need a versatile banner ad that I can add the DJ image to an area and then the date and time. I would assume we would agree the area where I can just add a layer via Photoshop with the DJ image and time info as I have more DJs. I will add one of my DJs images. You can crop as necessary. His airplay time is Friday 2pm set and 8pm set.

This is a DANCE radio station, so bright lights, lasers, etc will all be considered.

The banner size is 960X340

Target Market(s)

LGBT between 16-45

Industry/Entity Type

Radio

Requirements
Should not have
• although this is for LGBT, I do not want to see rainbow flags, headphones or other cheesy common themes

```html
<!DOCTYPE html>
<html lang="en">
<head>
<meta charset="utf-8">
<title>Deep Orbit Banner</title>
<link href="https://fonts.googleapis.com/css2?family=Lobster&family=Marcellus&display=swap" rel="stylesheet">
<style>
  :root {
    --page-bg: #1c1c1c;
    --banner-yellow: #f2ea1e;
    --banner-frame: #ffffff;
    --crowd-black: #050505;
    --photo-dark: #4a4440;
    --photo-light: #8a7e74;
    --title-red: #c8252a;
    --title-blue: #1778c2;
    --title-white: #ffffff;
    --title-black: #0a0a0a;
    --date-white: #ffffff;
    --date-blue: #1f7cc4;
  }
  * { margin: 0; padding: 0; box-sizing: border-box; }
  html, body {
    width: 1200px;
    height: 1000px;
    overflow: hidden;
    background: var(--page-bg);
  }
  .banner {
    position: absolute;
    left: 124px;
    top: 327px;
    width: 961px;
    height: 340px;
    background: var(--banner-yellow);
    border: 2px solid var(--banner-frame);
    border-bottom: none;
    overflow: hidden;
  }
  .crowd-art {
    position: absolute;
    left: 0;
    top: 60px;
    width: 100%;
    height: 280px;
    background: linear-gradient(to bottom, rgba(5,5,5,0) 0%, rgba(5,5,5,0.35) 45%, var(--crowd-black) 80%);
  }
  .dj-photo {
    position: absolute;
    left: 6px;
    top: 0;
    width: 226px;
    height: 340px;
    background: linear-gradient(to bottom, var(--photo-light) 0%, var(--photo-dark) 100%);
  }
  .title {
    position: absolute;
    font-family: "Lobster", cursive;
    font-weight: 400;
    paint-order: stroke fill;
    line-height: 1;
    white-space: nowrap;
  }
  .title-first {
    left: 318px;
    top: 86px;
    font-size: 112px;
    color: var(--title-white);
    -webkit-text-stroke: 16px var(--title-red);
    transform: rotate(-6deg);
  }
  .title-second {
    left: 574px;
    top: 34px;
    font-size: 122px;
    color: var(--title-black);
    -webkit-text-stroke: 16px var(--title-blue);
    transform: rotate(-9deg);
    transform-origin: center center;
  }
  .airtime {
    position: absolute;
    left: 414px;
    top: 270px;
    font-family: "Marcellus", serif;
    font-size: 44px;
    line-height: 1;
    color: var(--date-white);
    white-space: nowrap;
    letter-spacing: -0.5px;
  }
  .airtime-date { color: var(--date-blue); }
</style>
</head>
<body>
  <section class="banner">
    <div class="crowd-art" role="img" aria-label="Black silhouettes of a dancing crowd with a DJ at decks"></div>
    <div class="dj-photo" role="img" aria-label="Photo of the featured DJ"></div>
    <span class="title title-first">Deep</span>
    <span class="title title-second">Orbit</span>
    <p class="airtime">Friday <span class="airtime-date">26Jul</span> 2pm</p>
  </section>
</body>
</html>
```